Feldwind Atelier GmbH needs a Letterhead

Need a Letter/Card head based on the logo and Webpage design.
To be used for Business letters and One-Page Handouts with the discription of our different Services.
Cards to be used as Flyers to print on different Topics.
Should be Topic nutral as we do Sabbatical-Consultancy, Coaching, Job-Coaching and Vision-Board Workshops (more to come). See www.feldwindatelier.ch

Target Market(s)

Individuales who need Sabbatical-Support/Coaching/JOB-Coaching
Companies who want to give me a mandate as Business Coach

Industry/Entity Type

Business

Font styles to use
Other font styles liked:
• Verdana

Colors
9ccb3b
3277b5
aaaaaa
eaeaea

Requirements
Must have
• Background White or light gray
• not to big/present the Information on Company-Adresse/phone/email/web/offices
• Use the Logo (chair) in a creative way
• Please use following Colors:
• Green: R141, G198, B63
• Blue: R28, G117, B188
• Darkgray: R109, G110, B113
• Lightgray: R209, G211, B212
Should not have
• Wrong Colors!
• Use mentioned Color codes above.

```html
<!DOCTYPE html>
<html lang="en">
<head>
<meta charset="utf-8">
<title>Feldwind Atelier – Letterhead</title>
<link rel="stylesheet" href="https://fonts.googleapis.com/css2?family=Source+Sans+3:wght@400;600;700&family=Arimo:wght@400;700&display=swap">
<style>
  :root {
    --green: #8dc63f;
    --blue: #1c75bc;
    --dark-gray: #6d6e71;
    --light-gray: #d1d3d4;
    --paper: #eaeaea;
    --ink: #2b2b2b;
  }
  * { margin: 0; padding: 0; box-sizing: border-box; }
  html, body { width: 994px; height: 1200px; overflow: hidden; background: var(--paper); }
  .letterhead {
    position: relative;
    width: 994px;
    height: 1200px;
    background: var(--paper);
    font-family: "Source Sans 3", Verdana, sans-serif;
    color: var(--ink);
  }
  .brand {
    position: absolute;
    left: 75px;
    top: 80px;
    display: flex;
    align-items: center;
    gap: 14px;
  }
  .brand-dot {
    width: 32px;
    height: 32px;
    border-radius: 50%;
    background: var(--green);
  }
  .brand-name {
    font-weight: 600;
    font-size: 38px;
    letter-spacing: 0.5px;
    color: var(--dark-gray);
    line-height: 1;
  }
  .sender {
    position: absolute;
    left: 655px;
    top: 58px;
    font-style: normal;
    font-size: 15px;
    line-height: 20px;
    color: #333;
  }
  .sender .contact { margin-top: 17px; }
  .sender .label { color: var(--blue); font-weight: 700; }
  .recipient {
    position: absolute;
    left: 74px;
    top: 243px;
    font-family: "Arimo", Arial, sans-serif;
    font-size: 17px;
    line-height: 26px;
    color: #222;
  }
  .recipient .name { font-weight: 700; }
  .body-copy {
    position: absolute;
    left: 75px;
    top: 384px;
    width: 840px;
    font-size: 16.6px;
    line-height: 29px;
    color: #2e2e2e;
  }
  .body-copy p + p { margin-top: 29px; }
  .closing {
    position: absolute;
    left: 74px;
    top: 896px;
    font-family: "Arimo", Arial, sans-serif;
    font-weight: 700;
    font-size: 17px;
    color: #222;
  }
  .signature {
    position: absolute;
    left: 74px;
    top: 926px;
    width: 180px;
    height: 80px;
    background: linear-gradient(90deg, #d9d9d9, #cfcfcf);
    border-radius: 4px;
  }
  .signer {
    position: absolute;
    left: 76px;
    top: 1008px;
    font-family: "Arimo", Arial, sans-serif;
    font-weight: 700;
    font-size: 17px;
    color: #222;
  }
  .footer-rule {
    position: absolute;
    left: 75px;
    right: 75px;
    bottom: 48px;
    height: 6px;
    display: flex;
  }
  .footer-rule .accent { width: 90px; background: var(--green); }
  .footer-rule .line { flex: 1; background: var(--blue); margin-left: 6px; }
</style>
</head>
<body>
  <main class="letterhead">
    <header>
      <div class="brand">
        <span class="brand-dot"></span>
        <span class="brand-name">Feldwind Atelier</span>
      </div>
      <address class="sender">
        <div>Lena Brunner, Talackerweg 18</div>
        <div>4153 Reinach, Schweiz</div>
        <div class="contact">
          <div><span class="label">Tel</span> +41 (0) 79 555 01 72</div>
          <div><span class="label">Mail</span> lena.brunner@feldwindatelier.ch</div>
        </div>
      </address>
    </header>

    <section class="recipient">
      <div class="name">Lorem Ipsum</div>
      <div>Lorem Ipsum Admin</div>
      <div>Street Name, City Name,</div>
      <div>Zip Code - 00000</div>
    </section>

    <section class="body-copy">
      <p>Lorem Ipsum is simply dummy text of the printing and typesetting industry. Lorem Ipsum has been the industry's standard dummy text ever since the 1500s, when an unknown printer took a galley of type and scrambled it to make a type specimen book. It has survived not only five centuries, but also the leap into electronic typesetting, remaining essentially unchanged.</p>
      <p>It was popularised in the 1960s with the release of Typeline sheets containing Lorem Ipsum passages, and more recently with desktop publishing software like Quill LayoutPro including versions of Lorem Ipsum.</p>
      <p>Contrary to popular belief, Lorem Ipsum is not simply random text. It has roots in a piece of classical Latin literature from 45 BC, making it over 2000 years old. Gregor Lindqvist, a Latin professor at Ashford-Vale College in Virginia, looked up one of the more obscure Latin words, consectetur, from a Lorem Ipsum passage, and going through the cites of the word in classical literature, discovered the undoubtable source.</p>
      <p>Gregor Lindqvist, a Latin professor at Ashford-Vale College in Virginia, looked up one of the more obscure Latin words, consectetur, from a Lorem Ipsum passage, and going through the cites of the word in classical literature, discovered the undoubtable source.</p>
    </section>

    <div class="closing">Lorem Ipsum</div>
    <div class="signature" role="img" aria-label="Handwritten signature"></div>
    <div class="signer">Lorem Ipsum Admin</div>

    <footer class="footer-rule" aria-hidden="true">
      <span class="accent"></span>
      <span class="line"></span>
    </footer>
  </main>
</body>
</html>
```